Lantern Hearthworks Business Cards

Looking to create simple business cards that highlight our unique three sided triangle fire pit design with the colors and font of our logo, listed below.

Requirements
Must have
• Looking for something simple that includes a picture of our fire pit with name, website (lanternhearthworks.com), phone number and email. Want to keep the color mostly orange and black.
• Font is gotham(medium) and orange color code is #ee6e22

```html
<!DOCTYPE html>
<html lang="en">
<head>
<meta charset="utf-8">
<title>Lantern Hearthworks Business Cards</title>
<link rel="stylesheet" href="https://fonts.googleapis.com/css2?family=Montserrat:wght@500;600&display=swap">
<style>
  :root {
    --orange: #ee6e22;
    --charcoal: #2a2a2a;
    --grey: #5e5e5e;
    --rule: #b8b8b8;
    --paper: #ffffff;
    --stage: #e9e9e9;
    --card-black: #1c1c1c;
  }
  html, body {
    margin: 0;
    padding: 0;
    width: 1200px;
    height: 1108px;
    overflow: hidden;
    background: var(--stage);
    font-family: "Montserrat", Arial, sans-serif;
  }
  .canvas {
    position: relative;
    width: 1200px;
    height: 1108px;
    display: flex;
    justify-content: center;
    align-items: center;
    gap: 80px;
  }
  .card {
    position: relative;
    width: 400px;
    height: 660px;
    border-radius: 26px;
    overflow: hidden;
    box-shadow: 0 10px 30px rgba(0,0,0,0.18);
  }

  /* Front */
  .card-front {
    background: var(--paper);
    display: flex;
    flex-direction: column;
    align-items: center;
    text-align: center;
  }
  .wordmark {
    margin-top: 190px;
    color: var(--orange);
    font-weight: 500;
    font-size: 34px;
    line-height: 1.15;
    letter-spacing: 6px;
    text-transform: uppercase;
  }
  .holder-name {
    margin-top: 86px;
    color: var(--orange);
    font-weight: 600;
    font-size: 19px;
    letter-spacing: 0.5px;
    text-transform: uppercase;
  }
  .icon-row {
    margin-top: 20px;
    display: flex;
    align-items: center;
    gap: 6px;
  }
  .icon-row .rule {
    width: 50px;
    height: 1px;
    background: var(--rule);
    margin: 0 6px;
  }
  .icon-row svg { display: block; }
  .contact {
    margin-top: 14px;
    color: var(--grey);
    font-weight: 500;
    font-size: 17px;
    line-height: 1.45;
    text-transform: uppercase;
  }

  /* Back */
  .card-back {
    background: radial-gradient(ellipse at 40% 40%, #3a3a3a 0%, var(--card-black) 75%);
  }
  .back-wordmark {
    position: absolute;
    top: 76px;
    left: 0;
    right: 0;
    text-align: center;
    color: #9a9a9a;
    font-weight: 500;
    font-size: 32px;
    line-height: 1.15;
    letter-spacing: 6px;
    text-transform: uppercase;
  }
  .firepit-photo {
    position: absolute;
    left: 70px;
    top: 200px;
    width: 330px;
    height: 360px;
    background:
      radial-gradient(ellipse at 62% 42%, #ffb14a 0%, var(--orange) 28%, #8a3510 52%, rgba(20,20,20,0) 72%),
      linear-gradient(160deg, #2f2f2f 0%, #121212 100%);
  }
</style>
</head>
<body>
  <main class="canvas">
    <section class="card card-front">
      <div class="wordmark">Lantern<br>Hearthworks</div>
      <div class="holder-name">Daniel Reyes</div>
      <div class="icon-row">
        <span class="rule"></span>
        <svg width="24" height="24" viewBox="0 0 24 24" aria-label="Phone">
          <rect width="24" height="24" rx="3" fill="var(--orange)"/>
          <path d="M8 6c1 0 2 2 2 3s-1 1-1 2 3 4 4 4 1-1 2-1 3 1 3 2-1 2-2 2C10 18 6 14 6 8c0-1 1-2 2-2z" fill="#fff"/>
        </svg>
        <svg width="24" height="24" viewBox="0 0 24 24" aria-label="Email">
          <rect width="24" height="24" rx="3" fill="var(--orange)"/>
          <rect x="5" y="7" width="14" height="10" fill="none" stroke="#fff" stroke-width="1.6"/>
          <path d="M5 7l7 6 7-6" fill="none" stroke="#fff" stroke-width="1.6"/>
        </svg>
        <svg width="24" height="24" viewBox="0 0 24 24" aria-label="Website">
          <rect width="24" height="24" rx="3" fill="var(--orange)"/>
          <circle cx="12" cy="12" r="6.5" fill="none" stroke="#fff" stroke-width="1.5"/>
          <ellipse cx="12" cy="12" rx="3" ry="6.5" fill="none" stroke="#fff" stroke-width="1.2"/>
          <line x1="5.5" y1="12" x2="18.5" y2="12" stroke="#fff" stroke-width="1.2"/>
        </svg>
        <span class="rule"></span>
      </div>
      <div class="contact">
        044-555 012 347<br>
        hello@lanternhearthworks.com<br>
        www.lanternhearthworks.com
      </div>
    </section>

    <section class="card card-back">
      <div class="back-wordmark">Lantern<br>Hearthworks</div>
      <div class="firepit-photo" role="img" aria-label="Photo of a three-sided triangular steel fire pit with logs burning in bright orange flames on dark gravel"></div>
    </section>
  </main>
</body>
</html>
```